Boutique Real Estate Brokerage looking for business card, letterhead and envelope design

We are looking for a cohesive design for our business cards, letterhead and envelopes and that mirrors our high-end homes and clientele. Cedar & Vale is being launched and designed for the marketplace of tomorrow. We grew from the #1 team in our community into a full-service firm that is going to revolutionize the traditional real estate model.

We understand that it’s more important than ever to help our clients and partners adapt to behavioral and market changes being driven by generational shifts and technological advances in society, and by combining traditional brokerage services with innovative production and marketing capabilities, we know how to do that better than anyone else.

Requirements
Must have
• business card, letterhead and envelope design - attached logo.

```html
<!DOCTYPE html>
<html lang="en">
<head>
<meta charset="utf-8">
<title>Cedar &amp; Vale Realty – Stationery</title>
<link rel="stylesheet" href="https://fonts.googleapis.com/css2?family=Montserrat:wght@400;500;700&family=Roboto:wght@400&display=swap">
<style>
:root{
  --backdrop:#eceef1;
  --paper:#e8e9ec;
  --gold:#c3a05d;
  --purple:#33245f;
  --ink:#2a2a33;
  --label:#7d7f84;
}
*{margin:0;padding:0;box-sizing:border-box}
html,body{width:1200px;height:901px;overflow:hidden}
body{background:var(--backdrop);font-family:"Montserrat",sans-serif;color:var(--ink);position:relative}
.label{position:absolute;font-family:"Roboto",sans-serif;color:var(--label);font-size:15px;transform:translateX(-50%);white-space:nowrap}
.label.small{font-size:7px}
.sheet{position:absolute;background:var(--paper);box-shadow:0 3px 10px rgba(0,0,0,.12);overflow:hidden}
.band{position:absolute;left:0;bottom:0;width:100%;display:block}
.brand{position:absolute;display:flex;align-items:center;gap:5px;white-space:nowrap}
.brand-square{background:var(--purple);display:block}
.brand-name{font-weight:700;color:var(--purple);letter-spacing:.2px}
.contact{position:absolute;font-size:4.6px;line-height:6.6px;color:var(--ink);font-family:"Roboto",sans-serif}
.contact .row{display:flex;align-items:center;gap:3px;white-space:nowrap}
.contact svg{width:5px;height:5px;flex:none}
.address{position:absolute;display:flex;gap:3px;font-size:4.6px;line-height:5.6px;font-family:"Roboto",sans-serif;white-space:nowrap}
.address svg{width:5px;height:7px;flex:none}
.person .name{font-weight:700;font-size:8px}
.person .role{font-size:6px;font-weight:500}
</style>
</head>
<body>

<svg width="0" height="0" style="position:absolute">
  <defs>
    <symbol id="i-phone" viewBox="0 0 10 10"><path d="M1 4c0-2 2-3 4-3s4 1 4 3l-2 .5-.5-1.5h-3L3 4.5z M2.5 5h5l1 4h-7z" fill="#c3a05d"/></symbol>
    <symbol id="i-mail" viewBox="0 0 10 10"><rect x="1" y="2" width="8" height="6" rx="1" fill="#c3a05d"/><path d="M1.5 2.5 5 5.5 8.5 2.5" stroke="#e8e9ec" stroke-width=".8" fill="none"/></symbol>
    <symbol id="i-web" viewBox="0 0 10 10"><circle cx="5" cy="5" r="4" fill="#c3a05d"/><path d="M1 5h8M5 1c-2 2-2 6 0 8M5 1c2 2 2 6 0 8" stroke="#e8e9ec" stroke-width=".6" fill="none"/></symbol>
    <symbol id="i-pin" viewBox="0 0 10 14"><path d="M5 13C2 8.5 1 7 1 5a4 4 0 0 1 8 0c0 2-1 3.5-4 8z" fill="#c3a05d"/><circle cx="5" cy="5" r="1.6" fill="#e8e9ec"/></symbol>
  </defs>
</svg>

<!-- Letterhead -->
<div class="label" style="left:390px;top:40px">Letterhead</div>
<section class="sheet letterhead" style="left:214px;top:76px;width:367px;height:521px">
  <div class="brand" style="left:21px;top:22px"><span class="brand-square" style="width:22px;height:22px"></span><span class="brand-name" style="font-size:13px">CEDAR &amp; VALE</span></div>
  <div class="contact" style="left:230px;top:26px">
    <div class="row"><svg><use href="#i-phone"/></svg>01632 960418</div>
    <div class="row"><svg><use href="#i-mail"/></svg>info@cedarvale.com</div>
    <div class="row"><svg><use href="#i-web"/></svg>www.cedarvale.com</div>
  </div>
  <div class="address" style="left:286px;top:27px"><svg><use href="#i-pin"/></svg><div>Larch House, Elmfield Park<br>Mill Road, Halton<br>Westshire, WS12 3QR</div></div>
  <svg class="band" viewBox="0 0 367 10" height="10" preserveAspectRatio="none"><polygon points="0,0 180,0 190,10 0,10" fill="var(--gold)"/><polygon points="182,0 367,0 367,10 193,10" fill="var(--purple)"/></svg>
</section>

<!-- Compliments slip -->
<div class="label" style="left:900px;top:200px">Complimentary Slip</div>
<section class="sheet slip" style="left:658px;top:238px;width:483px;height:226px">
  <div class="brand" style="left:16px;top:20px"><span class="brand-square" style="width:21px;height:21px"></span><span class="brand-name" style="font-size:12px">CEDAR &amp; VALE</span></div>
  <div class="person" style="position:absolute;left:16px;top:160px"><div class="name">Marcus Ellery</div><div class="role">Managing Director</div></div>
  <div class="contact" style="left:16px;top:186px">
    <div class="row"><svg><use href="#i-phone"/></svg>01632 960418</div>
    <div class="row"><svg><use href="#i-mail"/></svg>info@cedarvale.com</div>
    <div class="row"><svg><use href="#i-web"/></svg>www.cedarvale.com</div>
  </div>
  <div class="address" style="left:84px;top:187px"><svg><use href="#i-pin"/></svg><div>Larch House, Elmfield Park<br>Mill Road, Halton<br>Westshire, WS12 3QR</div></div>
  <svg class="band" viewBox="0 0 483 7" height="7" preserveAspectRatio="none"><polygon points="0,0 238,0 246,7 0,7" fill="var(--gold)"/><polygon points="240,0 483,0 483,7 249,7" fill="var(--purple)"/></svg>
</section>

<!-- Business card -->
<div class="label" style="left:166px;top:605px">Business Card</div>
<div class="label small" style="left:166px;top:628px">Back</div>
<section class="sheet card-back" style="left:79px;top:638px;width:173px;height:98px;border-radius:4px">
  <div class="brand" style="left:28px;top:36px"><span class="brand-square" style="width:22px;height:22px"></span><span class="brand-name" style="font-size:11px">CEDAR &amp; VALE</span></div>
</section>
<div class="label small" style="left:166px;top:749px">Front</div>
<section class="sheet card-front" style="left:79px;top:759px;width:173px;height:98px;border-radius:4px">
  <div class="brand" style="left:11px;top:16px;gap:3px"><span class="brand-square" style="width:13px;height:13px"></span><span class="brand-name" style="font-size:7px">CEDAR &amp; VALE</span></div>
  <div class="person" style="position:absolute;left:95px;top:14px"><div class="name" style="font-size:6.5px">Marcus Ellery</div><div class="role" style="font-size:4.5px">Managing Director</div></div>
  <div class="address" style="left:11px;top:66px;font-size:3.6px;line-height:4.4px"><svg><use href="#i-pin"/></svg><div>Larch House, Elmfield Park<br>Mill Road, Halton<br>Westshire, WS12 3QR</div></div>
  <div class="contact" style="left:95px;top:65px;font-size:3.6px;line-height:5.2px">
    <div class="row"><svg style="width:4px;height:4px"><use href="#i-phone"/></svg>01632 960418</div>
    <div class="row"><svg style="width:4px;height:4px"><use href="#i-mail"/></svg>info@cedarvale.com</div>
    <div class="row"><svg style="width:4px;height:4px"><use href="#i-web"/></svg>www.cedarvale.com</div>
  </div>
  <svg class="band" viewBox="0 0 173 7" height="7" preserveAspectRatio="none"><polygon points="0,0 84,0 90,7 0,7" fill="var(--gold)"/><polygon points="86,0 173,0 173,7 92,7" fill="var(--purple)"/></svg>
</section>

<!-- Envelope front -->
<div class="label" style="left:495px;top:634px">Envelope Front</div>
<section class="sheet envelope-front" style="left:290px;top:654px;width:410px;height:198px">
  <div class="brand" style="left:20px;top:29px"><span class="brand-square" style="width:21px;height:21px"></span><span class="brand-name" style="font-size:12px">CEDAR &amp; VALE</span></div>
  <div class="contact" style="left:20px;top:158px">
    <div class="row"><svg><use href="#i-phone"/></svg>01632 960418</div>
    <div class="row"><svg><use href="#i-mail"/></svg>info@cedarvale.com</div>
    <div class="row"><svg><use href="#i-web"/></svg>www.cedarvale.com</div>
  </div>
  <div class="address" style="left:88px;top:159px"><svg><use href="#i-pin"/></svg><div>Larch House, Elmfield Park<br>Mill Road, Halton<br>Westshire, WS12 3QR</div></div>
  <svg class="band" viewBox="0 0 410 7" height="7" preserveAspectRatio="none"><polygon points="0,0 202,0 210,7 0,7" fill="var(--gold)"/><polygon points="205,0 410,0 410,7 214,7" fill="var(--purple)"/></svg>
</section>

<!-- Envelope back -->
<div class="label" style="left:945px;top:634px">Envelope Back</div>
<section class="sheet envelope-back" style="left:736px;top:654px;width:416px;height:198px;background:#ececef">
  <svg viewBox="0 0 416 198" width="416" height="198" style="position:absolute;left:0;top:0">
    <polygon points="0,0 172,0 240,70 12,72" fill="var(--gold)"/>
    <polygon points="176,0 416,0 412,68 244,70" fill="var(--purple)"/>
  </svg>
</section>

</body>
</html>
```